Home page makeover

Take my existing home page, www.maplecrestharborline.com and redesign layout to look more current considering today's touch design prevalence.
Reuse existing elements or suggest improved ones if available.
I generally have average CSS and HTML skills using div containers, defining lists and using columns to create the code to support the layout.
Updates
Just wanted to send out a quick message to thank all of you for your submissions. Many of you offered nice designs, but unfortunately could only choose one.
Target Market(s)
Generally targeting individuals with some assets for retirement. Basically your average working professional or business owner.
Industry/Entity Type
It Support
Look and feel
Each slider illustrates characteristics of the customer's brand and the style your logo design should communicate.

```html
<!DOCTYPE html>
<html lang="en">
<head>
<meta charset="utf-8">
<title>Maplecrest Harborline Planner</title>
<link rel="stylesheet" href="https://fonts.googleapis.com/css2?family=Cinzel:wght@400;700&family=PT+Sans:wght@400;700&display=swap">
<style>
:root{
  --bg:#f7f7f7;
  --ink:#333;
  --muted:#666;
  --green-dark:#2f5a14;
  --green:#a6bf3b;
  --green-light:#c2d36a;
  --panel:#3a3a3a;
  --line:#111;
}
*{margin:0;padding:0;box-sizing:border-box}
html,body{width:711px;height:1200px;overflow:hidden;background:var(--bg)}
body{position:relative;font-family:"PT Sans",sans-serif;color:var(--ink)}
.abs{position:absolute}
.serif{font-family:"Cinzel",serif}

/* header */
.brand{left:70px;top:18px;display:flex;align-items:center;gap:8px}
.brand-mark{width:30px;height:30px;background:var(--green-dark)}
.brand-name{font-family:"Cinzel",serif;font-size:13px;line-height:15px;color:var(--green-dark);letter-spacing:.5px}
.account{top:13px;height:16px;font:400 8px/16px "Cinzel",serif;color:#fff;text-align:center;letter-spacing:.5px}
.account.signup{left:522px;width:58px;background:var(--green-dark)}
.account.signin{left:583px;width:57px;background:var(--green)}
.nav{top:50px;left:345px;display:flex;height:32px}
.nav a{font:400 9.5px/32px "Cinzel",serif;color:#333;text-decoration:none;letter-spacing:.5px}
.nav .active{background:var(--green);color:#333;padding:0 12px;width:58px;text-align:center}
.nav .i1{margin-left:8px}.nav .i2{margin-left:22px}.nav .i3{margin-left:23px}.nav .i4{margin-left:21px}
.rule{left:0;top:82px;width:711px;height:3px;background:var(--line)}

/* hero */
.hero{left:0;top:85px;width:711px;height:320px;background:linear-gradient(100deg,#b9c4d4 0%,#e6d3c4 40%,#efe9e0 60%,#3b3b3e 80%,#2c2c2e 100%)}
.offer{left:70px;top:223px;width:231px;height:95px;background:rgba(58,58,58,.93);padding:18px 14px;color:#fff;font-size:11px;line-height:20px}
.offer b{color:var(--green)}
.offer .cta{display:inline-block;margin-top:8px;background:var(--green);color:#fff;font:700 10.5px/16px "PT Sans",sans-serif;padding:0 10px}
.dots{left:334px;top:379px;display:flex;gap:3px}
.dots span{width:9px;height:9px;border-radius:50%;background:#555}
.dots span:first-child{background:var(--green)}

/* sections */
.heading{left:0;width:711px;text-align:center;font:700 11.5px "Cinzel",serif;color:var(--green-dark);letter-spacing:.6px}
.intro{left:77px;top:455px;width:557px;text-align:center;font-size:7px;line-height:14px;color:var(--muted)}
.service{top:552px;width:179px}
.service h3{font:400 9.5px "Cinzel",serif;color:#333;letter-spacing:.4px;margin-bottom:5px}
.service .photo{width:179px;height:113px;border:1px solid #ccc}
.service p{margin-top:14px;font-size:7px;line-height:14px;color:var(--muted)}
.service .more{display:inline-block;margin-top:8px;background:var(--green);color:#fff;font:400 7.5px/16px "Cinzel",serif;padding:0 6px;letter-spacing:.4px}
.features-title{left:77px;top:820px;font:700 11.5px "Cinzel",serif;color:var(--green-dark);letter-spacing:.6px}
.video{left:78px;top:846px;width:331px;height:178px;background:linear-gradient(135deg,#8fb35a 0%,#d9c8a8 45%,#e8d2b8 60%,#a9c46e 100%)}
.player{left:95px;top:999px;width:297px;height:18px;background:rgba(40,40,40,.85);border-radius:3px}
.player .track{position:absolute;left:6px;top:6px;width:216px;height:6px;background:#555}
.player .track i{display:block;width:60px;height:6px;background:#2a9ad6}
.player .hd{position:absolute;left:257px;top:3px;font:700 italic 9px "PT Sans",sans-serif;color:#2a9ad6}
.play{left:224px;top:921px;width:38px;height:24px;background:rgba(30,30,30,.85);border-radius:5px}
.feature-list{left:419px;top:850px;width:215px;list-style:none}
.feature-list li{position:relative;padding-left:19px;font-size:6.9px;line-height:11px;color:#444;margin-bottom:9px}
.feature-list li::before{content:"";position:absolute;left:0;top:1px;width:10px;height:10px;border-radius:50%;background:var(--green)}
.feature-list li::after{content:"";position:absolute;left:3px;top:4px;width:3px;height:3px;border-right:1.3px solid #fff;border-top:1.3px solid #fff;transform:rotate(45deg)}
.quote{left:0;top:1082px;width:711px;text-align:center;font-size:11px;color:#444}
.quote .who{font-size:13px;color:var(--green-dark)}
.quote .who b{font-size:11px}

/* footer */
.footer{left:0;top:1138px;width:711px;height:62px;background:var(--green)}
.footer-nav{left:77px;top:1154px;font:400 7.5px "Cinzel",serif;color:#fff;letter-spacing:.5px;word-spacing:2px}
.copyright{left:77px;top:1175px;font:400 7px "Cinzel",serif;color:#fff;letter-spacing:.4px}
.social{top:1160px;width:20px;height:20px;border-radius:50%;background:#fff}
</style>
</head>
<body>

<header>
  <div class="abs brand">
    <span class="brand-mark"></span>
    <span class="brand-name">Maplecrest Harborline<br>Planner</span>
  </div>
  <a class="abs account signup">SIGN UP</a>
  <a class="abs account signin">SIGN IN</a>
  <nav class="abs nav">
    <a class="active">HOME</a>
    <a class="i1">ABOUT US</a>
    <a class="i2">SERVICES</a>
    <a class="i3">FAQ'S</a>
    <a class="i4">CONTACT</a>
  </nav>
  <div class="abs rule"></div>
</header>

<section>
  <div class="abs hero" role="img" aria-label="Photo of a senior couple meeting with a financial advisor"></div>
  <div class="abs offer">
    Only <b>$19.99</b> For a One Year Membership<br>
    Only <b>$9.99</b> &nbsp;Per Year After That<br>
    <span class="cta">SIGN UP</span>
  </div>
  <div class="abs dots"><span></span><span></span><span></span><span></span></div>
</section>

<h2 class="abs heading" style="top:428px">WELCOME TO MAPLECREST HARBORLINE PLANNER</h2>
<p class="abs intro">Lorem Ipsum is simply dummy text of the printing and typesetting industry. Lorem Ipsum has been the industry's standard dummy text ever since the 1500s, when an unknown printer took a galley of type and scrambled it to make a type specimen book. It has survived not only five centuries, but also the leap into electronic typesetting, remaining essentially unchanged. It was popularised in the 1960s with the release of Letraset sheets containing Lorem Ipsum passages, and more recently with desktop publishing software like Aldus PageMaker including versions of Lorem Ipsum.</p>

<h2 class="abs heading" style="top:531px">OUR SERVICES</h2>
<div class="abs service" style="left:77px">
  <h3>INDENTIFY</h3>
  <div class="photo" role="img" aria-label="Photo of a pen, banknotes and financial charts" style="background:linear-gradient(135deg,#9aa48c,#e8e6da 60%,#cfd2c8)"></div>
  <p>Lorem Ipsum is simply dummy text of the printing and typesetting industry. Lorem Ipsum has been the indus-try's standard dummy text ever since the 1500s, when an unknown printer took a galley of type and scrambled it to make a type specimen book.</p>
  <span class="more">READ MORE</span>
</div>
<div class="abs service" style="left:266px">
  <h3>PLAN</h3>
  <div class="photo" role="img" aria-label="Photo of a laptop keyboard with reading glasses" style="background:linear-gradient(135deg,#2a2a2a,#8a8a8a 45%,#f2f2f2 70%)"></div>
  <p>Lorem Ipsum is simply dummy text of the printing and typesetting industry. Lorem Ipsum has been the indus-try's standard dummy text ever since the 1500s, when an unknown printer took a galley of type and scrambled it to make a type specimen book.</p>
  <span class="more">READ MORE</span>
</div>
<div class="abs service" style="left:457px">
  <h3>RETIRE</h3>
  <div class="photo" role="img" aria-label="Photo of a rope hammock on a seaside porch" style="background:linear-gradient(180deg,#7fa6cf,#b9cde0 45%,#d8c9a8 70%,#e9e4da)"></div>
  <p>Lorem Ipsum is simply dummy text of the printing and typesetting industry. Lorem Ipsum has been the indus-try's standard dummy text ever since the 1500s, when an unknown printer took a galley of type and scrambled it to make a type specimen book.</p>
  <span class="more">READ MORE</span>
</div>

<h2 class="abs features-title">FEATURES</h2>
<div class="abs video" role="img" aria-label="Video still of a smiling retired couple outdoors"></div>
<div class="abs play"><svg width="38" height="24"><polygon points="15,7 15,17 24,12" fill="#fff"/></svg></div>
<div class="abs player"><div class="track"><i></i></div><span class="hd">HD</span></div>
<ul class="abs feature-list">
  <li>Identify and project your retirement needs and expectations including basic living expenses, housing costs, recreation, big ticket non-recurring items, medical and nursing home care.</li>
  <li>Identify and project all your sources of retirement income including retirement savings, other savings, pension plans, Social Security, life insurance and working part-time during retirement for a period of time.</li>
  <li>Strategize tapping into the equity of your real estate including swapping your primary residence for a different home or retirement area, or selling and renting.</li>
  <li>Produce easy to understand results featuring the Readiness Gauge™.</li>
  <li>Save your work so you can return, revisit and edit your retire-ment plan at a later date.</li>
</ul>

<h2 class="abs heading" style="top:1055px">TESTIMONIALS</h2>
<p class="abs quote">“This site is a great place to get a handle on your retirement strategy”, <span class="who">Dana, <b>Vermont</b></span></p>

<footer>
  <div class="abs footer"></div>
  <div class="abs footer-nav">HOME &nbsp;| &nbsp;ABOUT US &nbsp;| &nbsp;SERVICES &nbsp;| &nbsp;FAQ'S &nbsp;| &nbsp;CONTACT</div>
  <div class="abs copyright">COPYRIGHT ©2013 COMPANY NAME &nbsp;- ALL RIGHTS RESERVED</div>
  <span class="abs social" style="left:595px" aria-label="Social link"></span>
  <span class="abs social" style="left:621px" aria-label="Social link"></span>
</footer>

</body>
</html>
```